Boutique Health and Fitness Personal Training Studio

I would like to have a brochure designed which provides a detailed description of the services offered in my business.
I have personal training studio, We look after people from early 20's to 90's, healthy to very unhealthy.
We conduct:
A consultation
An assessment
A personalised program
Personalised training sessions
I would like to base the design around the colours of my logo (attached) and use some of (or all of) the images and information I have also attached.
I would be happy with your own images included also.

Target Market(s)

20 to 90 year olds

Industry/Entity Type

Business

Font styles to use
Serif
Sans Serif

Colors
9bcb3c
add136
cadf82
eaf2ce

Requirements
Must have
• Colour and images of fitness.
• 8.5x14 legal
• Tri fold
• 2 folds with 3 faces back n front
Nice to have
• The feeling of wellbeing
Should not have
• This is not a gym.
• It should have the feel of a private relaxed environment

```html
<!DOCTYPE html>
<html lang="en">
<head>
<meta charset="utf-8">
<title>Verdant Studio – Tri-fold Brochure</title>
<link href="https://fonts.googleapis.com/css2?family=Questrial&family=Lato:wght@300;400&family=Arimo:wght@400;700&display=swap" rel="stylesheet">
<style>
  :root{
    --leaf:#9bcb3c;
    --lime:#add136;
    --pale:#cadf82;
    --mist:#eaf2ce;
    --forest:#6b9337;
    --deep:#3e6a1d;
    --ink:#4a4a4a;
    --backdrop:#262a2e;
    --paper:#ffffff;
  }
  *{box-sizing:border-box;margin:0;padding:0}
  html,body{width:1200px;height:1200px;overflow:hidden;background:var(--backdrop)}
  .sheet{position:absolute;left:126px;width:948px;height:575px;background:var(--paper);overflow:hidden}
  .sheet--outside{top:20px}
  .sheet--inside{top:605px}
  .sheet-art{position:absolute;inset:0;width:948px;height:575px}
  .block{position:absolute;font-family:"Lato",sans-serif;font-weight:400;color:var(--ink);font-size:9px;line-height:13px}
  .block--right{text-align:right}
  .heading{font-family:"Questrial",sans-serif;font-size:14.5px;color:var(--deep);line-height:18px;display:flex;align-items:center;gap:8px;margin-bottom:8px}
  .block--right .heading{justify-content:flex-end}
  .heading-dot{width:10px;height:10px;border-radius:50%;background:var(--forest);flex:none}
  .para + .para{margin-top:13px}
  .site-url{position:absolute;top:13px;right:24px;font-family:"Lato",sans-serif;font-size:7px;color:#8a8a8a}
  .brand{position:absolute;display:flex;align-items:center;gap:6px;font-family:"Questrial",sans-serif;color:var(--deep);white-space:nowrap;z-index:2}
  .brand-dot{border-radius:50%;background:var(--leaf);flex:none}
  .brand--small{left:344px;top:46px;font-size:14px}
  .brand--small .brand-dot{width:12px;height:12px}
  .brand--large{left:690px;top:52px;font-size:26px}
  .brand--large .brand-dot{width:24px;height:24px}
  .tagline{position:absolute;left:660px;width:256px;top:112px;text-align:center;font-family:"Questrial",sans-serif;font-weight:400;font-size:17.5px;line-height:20px;color:var(--deep)}
  .tagline-sub{position:absolute;left:660px;width:256px;top:155px;text-align:center;font-family:"Lato",sans-serif;font-weight:300;font-size:10.5px;line-height:13px;color:#555}
  .tagline-sub em{font-style:normal;color:var(--leaf)}
  .cost{position:absolute;left:27px;top:418px;color:#fff;font-family:"Questrial",sans-serif}
  .cost-title{font-size:17px;line-height:20px}
  .cost-price{font-size:11.5px;margin-top:8px}
  .cost-list{list-style:none;margin-top:17px;font-size:11.5px;line-height:17px}
  .cost-list li::before{content:"";display:inline-block;width:4px;height:4px;border-radius:50%;background:#fff;margin:0 8px 2px 2px;vertical-align:middle}
  .contact{position:absolute;left:330px;width:284px;top:477px;text-align:center;color:#fff;font-family:"Questrial",sans-serif;font-size:11px;line-height:16.5px}
  .contact-name{font-size:14px;margin-bottom:1px}
  .contact-phone{font-size:13px}
  .credentials{position:absolute;left:650px;width:276px;top:464px;text-align:center;color:#fff;font-family:"Arimo",sans-serif;font-size:9px;line-height:11.5px}
  .credentials strong{display:block;font-size:10.5px;margin:7px 0 6px}
  .credentials .years{font-size:11px}
</style>
</head>
<body>

<section class="sheet sheet--outside" aria-label="Brochure outside">
  <svg class="sheet-art" viewBox="0 0 948 575">
    <defs>
      <clipPath id="outside-lens"><path d="M0,322 C260,196 640,138 948,262 L948,372 C660,462 260,456 0,332 Z"/></clipPath>
      <linearGradient id="tone-gym" gradientUnits="userSpaceOnUse" x1="0" y1="200" x2="315" y2="470">
        <stop offset="0" stop-color="#3d4347"/><stop offset=".35" stop-color="#9a6a52"/><stop offset=".55" stop-color="#20262b"/><stop offset=".8" stop-color="#4d5a55"/><stop offset="1" stop-color="#2a2f33"/>
      </linearGradient>
      <linearGradient id="tone-outdoor" gradientUnits="userSpaceOnUse" x1="0" y1="50" x2="0" y2="470">
        <stop offset="0" stop-color="#7a4f3a"/><stop offset=".16" stop-color="#caa28a"/><stop offset=".34" stop-color="#d7b29a"/><stop offset=".5" stop-color="#b8bab4"/><stop offset=".72" stop-color="#9ea58a"/><stop offset=".86" stop-color="#a3403c"/><stop offset="1" stop-color="#7f6a4e"/>
      </linearGradient>
      <linearGradient id="tone-therapy" gradientUnits="userSpaceOnUse" x1="630" y1="0" x2="948" y2="0">
        <stop offset="0" stop-color="#2e3032"/><stop offset=".12" stop-color="#c9272f"/><stop offset=".45" stop-color="#d83a3c"/><stop offset=".6" stop-color="#d4a48e"/><stop offset=".75" stop-color="#f1f1f1"/><stop offset="1" stop-color="#e2e4e2"/>
      </linearGradient>
    </defs>
    <path d="M0,340 C260,466 660,472 948,380 L948,575 L0,575 Z" fill="var(--forest)"/>
    <path d="M0,310 C260,182 640,124 948,248 L948,386 C660,478 260,472 0,346 Z" fill="var(--lime)"/>
    <g clip-path="url(#outside-lens)">
      <rect role="img" aria-label="Photo: man training on a cable machine" x="0" y="150" width="315" height="350" fill="url(#tone-gym)"/>
      <rect role="img" aria-label="Photo: man doing push-ups outdoors" x="315" y="150" width="315" height="350" fill="url(#tone-outdoor)"/>
      <rect role="img" aria-label="Photo: physiologist treating a client's back" x="630" y="150" width="318" height="350" fill="url(#tone-therapy)"/>
    </g>
    <path d="M472,300 L472,110 Q472,50 532,50 L566,50 Q626,50 626,110 L626,200 Q630,240 630,260 L630,300 Z" fill="url(#tone-outdoor)"/>
  </svg>

  <div class="site-url">www.verdantstudio.com.au</div>

  <div class="block" style="left:27px;top:66px;width:200px">
    <div class="heading"><span class="heading-dot"></span>Your sessions</div>
    <p class="para">Training at the studio is professional and<br>caring, but focused and challenging.<br>Typically each session will take approximately<br>60 minutes.</p>
    <p class="para">Training times can be organized to suit<br>your needs with early mornings and<br>evenings available.</p>
  </div>

  <div class="brand brand--small"><span class="brand-dot"></span>Verdant Studio</div>
  <div class="brand brand--large"><span class="brand-dot"></span>Verdant Studio</div>

  <h1 class="tagline">Personalised Care in Fitness<br>and Health</h1>
  <p class="tagline-sub">Exercise programs for all levels of health<br>and fitness and <em>all age groups.</em></p>

  <div class="cost">
    <div class="cost-title">The Cost</div>
    <div class="cost-price">$45 paid in blocks of 5 or 10 sessions.</div>
    <ul class="cost-list">
      <li>Health fund claimable</li>
      <li>Open 7 days</li>
      <li>Ample private parking available</li>
    </ul>
  </div>

  <div class="contact">
    <div class="contact-name">Verdant Studio</div>
    <div>Suite 12, Level 2, 8 Wattle Grove Road, Greenvale</div>
    <div class="contact-phone">Ph: 0400 555 017</div>
    <div>www.verdantstudio.com.au</div>
  </div>

  <div class="credentials">
    Experience in managing a wide range of<br>chronic health conditions.
    <strong>Experienced professionals caring for your wellbeing</strong>
    Exercise Physiologist with over <span class="years">25 years</span><br>of experience managing the health and fitness<br>needs of the community.
  </div>
</section>

<section class="sheet sheet--inside" aria-label="Brochure inside">
  <svg class="sheet-art" viewBox="0 0 948 575">
    <defs>
      <linearGradient id="inside-wash" x1="0" y1="0" x2="0" y2="1"><stop offset=".3" stop-color="#ffffff"/><stop offset="1" stop-color="#d3e6a2"/></linearGradient>
      <clipPath id="inside-band"><path d="M0,0 H948 V160 C860,146 760,128 640,138 C520,148 450,198 340,203 C220,210 110,176 0,140 Z"/></clipPath>
      <clipPath id="below-band"><path d="M0,140 C110,176 220,210 340,203 C450,198 520,148 640,138 C760,128 860,146 948,160 V575 H0 Z"/></clipPath>
      <linearGradient id="tone-class" gradientUnits="userSpaceOnUse" x1="0" y1="0" x2="315" y2="0">
        <stop offset="0" stop-color="#ecebe8"/><stop offset=".2" stop-color="#d9b49c"/><stop offset=".38" stop-color="#3fa7d0"/><stop offset=".55" stop-color="#f2f2f2"/><stop offset=".75" stop-color="#e6c9b3"/><stop offset="1" stop-color="#d8dde0"/>
      </linearGradient>
      <linearGradient id="tone-measure" gradientUnits="userSpaceOnUse" x1="315" y1="0" x2="630" y2="0">
        <stop offset="0" stop-color="#f3efea"/><stop offset=".2" stop-color="#c9866a"/><stop offset=".45" stop-color="#e0b94a"/><stop offset=".6" stop-color="#c9323a"/><stop offset="1" stop-color="#b3262b"/>
      </linearGradient>
      <linearGradient id="tone-food" gradientUnits="userSpaceOnUse" x1="630" y1="0" x2="948" y2="0">
        <stop offset="0" stop-color="#6f8a3c"/><stop offset=".2" stop-color="#cf3b2a"/><stop offset=".4" stop-color="#e6c23a"/><stop offset=".6" stop-color="#9fa3a6"/><stop offset=".8" stop-color="#8c6a45"/><stop offset="1" stop-color="#c7b9a3"/>
      </linearGradient>
      <linearGradient id="tone-stretch" gradientUnits="userSpaceOnUse" x1="0" y1="80" x2="0" y2="270">
        <stop offset="0" stop-color="#e9d9c8"/><stop offset=".55" stop-color="#b9b6b0"/><stop offset=".75" stop-color="#8f9296"/><stop offset="1" stop-color="#4d80c2"/>
      </linearGradient>
      <linearGradient id="tone-cardio" x1="0" y1="0" x2="1" y2="0"><stop offset="0" stop-color="#4b5054"/><stop offset=".55" stop-color="#9aa4aa"/><stop offset="1" stop-color="#bcd8e6"/></linearGradient>
      <linearGradient id="tone-yoga" gradientUnits="userSpaceOnUse" x1="0" y1="90" x2="0" y2="225">
        <stop offset="0" stop-color="#d9a68a"/><stop offset=".45" stop-color="#f08fb6"/><stop offset=".7" stop-color="#e59ab8"/><stop offset="1" stop-color="#1e1e1e"/>
      </linearGradient>
      <linearGradient id="tone-silhouette" x1="0" y1="0" x2="0" y2="1"><stop offset="0" stop-color="#1f2419" stop-opacity=".55"/><stop offset=".4" stop-color="#1f2419" stop-opacity=".85"/><stop offset="1" stop-color="#15180f" stop-opacity=".95"/></linearGradient>
    </defs>
    <rect width="948" height="575" fill="url(#inside-wash)"/>
    <g clip-path="url(#inside-band)">
      <rect role="img" aria-label="Photo: group class lifting hand weights" x="0" y="0" width="315" height="230" fill="url(#tone-class)"/>
      <rect role="img" aria-label="Photo: waist being measured with a tape" x="315" y="0" width="315" height="230" fill="url(#tone-measure)"/>
      <rect role="img" aria-label="Photo: vegetables, water and dumbbells" x="630" y="0" width="318" height="230" fill="url(#tone-food)"/>
    </g>
    <path d="M0,140 C110,176 220,210 340,203 C450,198 520,148 640,138 C760,128 860,146 948,160 V178 C860,164 760,146 640,156 C520,166 450,216 340,221 C220,228 110,194 0,158 Z" fill="var(--pale)"/>
    <g clip-path="url(#below-band)">
      <path role="img" aria-label="Photo: older woman stretching on a mat" d="M185,80 H318 V240 Q318,268 290,268 H213 Q185,268 185,240 Z" fill="url(#tone-stretch)"/>
      <path role="img" aria-label="Photo: woman seated cross-legged holding weights" d="M787,90 H904 V196 Q904,222 878,222 H813 Q787,222 787,196 Z" fill="url(#tone-yoga)"/>
    </g>
    <circle role="img" aria-label="Photo: woman on a cross trainer" cx="391" cy="175" r="64" fill="url(#tone-cardio)" stroke="var(--pale)" stroke-width="6"/>
    <path role="img" aria-label="Silhouettes: trainer with exercise ball beside a woman" d="M165,575 V430 Q165,398 197,398 H272 Q304,398 304,430 V575 Z" fill="url(#tone-silhouette)"/>
    <path role="img" aria-label="Silhouettes: two people balancing on exercise balls" d="M340,575 V480 Q340,440 380,440 H572 Q612,440 612,480 V575 Z" fill="url(#tone-silhouette)"/>
    <path role="img" aria-label="Silhouettes: trainer guiding a lunge" d="M704,575 V448 Q704,416 736,416 H850 Q882,416 882,448 V575 Z" fill="url(#tone-silhouette)"/>
  </svg>

  <div class="block" style="left:27px;top:246px;width:200px">
    <div class="heading"><span class="heading-dot"></span>What to Expect</div>
    <p class="para">On arrival at the studio you will be<br>asked to complete a questionnaire, which<br>will provide us with information regarding<br>your background with health and fitness,<br>as well as your goals and objectives.</p>
    <p class="para">Please bring any relevant<br>medical information from medical<br>practitioners or health professionals<br>that you feel may impact on<br>your program.</p>
  </div>

  <div class="block block--right" style="left:402px;top:205px;width:200px">
    <div class="heading"><span class="heading-dot"></span>Consultation</div>
    <p class="para">A consultation will allow you to share your<br>thoughts, concerns and objectives,<br>as well as provide you with ample<br>opportunity to expand on the answers<br>from your questionnaire relating to<br>your prior and current health,<br>medical and physical concerns.</p>
  </div>

  <div class="block" style="left:341px;top:318px;width:240px">
    <div class="heading"><span class="heading-dot"></span>Assessment</div>
    <p class="para">An assessment will be conducted to provide us<br>both with a baseline measure of your cardiovascular<br>fitness, strength, flexibility, balance and body<br>composition measures.<br>These measures provide us with a reference<br>for program design and also to indicate<br>improvements along the way.</p>
  </div>

  <div class="block" style="left:655px;top:202px;width:240px">
    <div class="heading"><span class="heading-dot"></span>The program</div>
    <p class="para">Your program will be designed with consideration to<br>your health and fitness background, your objectives<br>and your strengths and weaknesses. It will be personally<br>tailored to your needs and provide you with a<br>plan to focus your energies on.</p>
  </div>

  <div class="block block--right" style="left:679px;top:301px;width:240px">
    <div class="heading"><span class="heading-dot"></span>Nutrition</div>
    <p class="para">Nutrition is central to an effective program, as it will<br>provide you with maximal energy for exercise<br>as well as keeping yourself lean and healthy<br>for a long term fitter lifestyle.<br>Verdant Studio provides initial monitoring and<br>ongoing modification in accordance with your needs.</p>
  </div>
</section>

</body>
</html>
```